Baby acupressure app for parents

We need an app for parents that teaches parents how to help them relieve their baby's imbalances (stomach ache, trouble sleeping etc.)

Please see the attached document (with info) and wireframes.

This project is urgent so please only participate if you're able to finish all screens within a few days after the contest is over.

Target Market(s)

Baby moms (20-40 years of age)

Industry/Entity Type

Baby Care

Colors
886aae
b768aa
e667a6
f68d4d
faa54b
fac994
f9ba93
f59195
fee18a

Requirements
Must have
• A high quality design that is both modern and very sleek and stylish.
Nice to have
• Simple animations to make the app "feel" like it's extreme high quality and make the user want to use it again and again
Should not have
• Sandwich menus

```html
<!DOCTYPE html>
<html lang="en">
<head>
<meta charset="UTF-8">
<title>Growing Pains – app screen</title>
<link href="https://fonts.googleapis.com/css2?family=Varela+Round&display=swap" rel="stylesheet">
<style>
  :root {
    --bg-light: #f4f4f5;
    --bg-mid: #e4e4e7;
    --ink: #2f2a3d;
    --body-ink: #222222;
    --purple: #8f66b6;
    --purple-deep: #64449a;
    --badge-blue: #6fb4df;
    --screen: #ffffff;
    --photo-cream: #f7f2f1;
    --photo-pink: #efc4bd;
    --photo-rose: #e3a9a2;
    --photo-skin: #f3d2bd;
    --photo-warm: #d8b48c;
    --photo-shadow: #b98f6a;
  }
  * { box-sizing: border-box; margin: 0; padding: 0; }
  html, body { width: 1200px; height: 1200px; overflow: hidden; }
  body {
    font-family: "Varela Round", "Helvetica Neue", Arial, sans-serif;
    background: linear-gradient(135deg, var(--bg-light) 0%, var(--bg-mid) 55%, var(--bg-light) 100%);
    position: relative;
  }

  .app-screen {
    position: absolute;
    left: 186px; top: 144px;
    width: 370px; height: 664px;
    background: var(--screen);
    border-radius: 6px;
    overflow: hidden;
    box-shadow: 0 14px 40px rgba(40,30,60,0.12);
  }
  .status-bar {
    position: absolute; top: 8px; left: 8px; right: 8px;
    display: flex; justify-content: space-between; align-items: center;
    font-size: 11px; color: var(--ink); z-index: 2;
  }
  .status-bar .signal { display: flex; gap: 2px; align-items: flex-end; }
  .status-bar .signal i { display: block; width: 2px; background: var(--ink); }
  .status-bar .battery { display: flex; align-items: center; gap: 4px; }
  .status-bar .battery-cell { width: 22px; height: 9px; border: 1px solid var(--ink); border-radius: 2px; padding: 1px; }
  .status-bar .battery-cell span { display: block; width: 100%; height: 100%; background: var(--ink); }

  .hero { position: absolute; top: 0; left: 0; width: 370px; height: 236px; }
  .back-arrow { position: absolute; top: 36px; left: 12px; z-index: 2; }
  .play-button { position: absolute; left: 161px; top: 118px; z-index: 2; }

  .article-title {
    position: absolute; left: 20px; top: 252px;
    font-size: 34px; font-weight: 400; color: var(--ink); letter-spacing: 0.2px;
  }
  .category-badge {
    position: absolute; left: 305px; top: 249px;
    width: 50px; height: 50px; border-radius: 50%;
    background: var(--badge-blue);
  }
  .article-text {
    position: absolute; left: 20px;
    width: 320px;
    font-size: 17px; line-height: 20px; color: var(--body-ink);
  }
  .article-text.intro { top: 312px; }
  .article-text.tips { top: 590px; }

  .inline-photo {
    position: absolute; left: 0; top: 418px; width: 370px; height: 148px;
    background:
      radial-gradient(ellipse 90px 60px at 140px 70px, var(--photo-skin) 0%, rgba(243,210,189,0) 100%),
      radial-gradient(ellipse 80px 55px at 290px 60px, var(--photo-skin) 0%, rgba(243,210,189,0) 100%),
      radial-gradient(ellipse 70px 40px at 60px 110px, #efcbb3 0%, rgba(239,203,179,0) 100%),
      linear-gradient(180deg, #e9d3bf 0%, var(--photo-warm) 100%);
  }

  .app-identity {
    position: absolute; left: 770px; top: 120px; width: 336px;
    display: flex; flex-direction: column; align-items: center;
  }
  .app-tile {
    width: 280px; height: 280px; border-radius: 48px;
    background: linear-gradient(180deg, var(--purple) 0%, var(--purple-deep) 100%);
  }
  .app-name {
    margin-top: 22px;
    font-size: 56px; line-height: 70px; color: var(--ink); letter-spacing: 0.5px;
  }
</style>
</head>
<body>

  <main class="app-screen">
    <svg class="hero" viewBox="0 0 370 236" role="img" aria-label="Photo of a newborn's feet held in a parent's cupped hands">
      <defs>
        <linearGradient id="heroBase" x1="0" y1="0" x2="1" y2="1">
          <stop offset="0" stop-color="#f7f2f1"/>
          <stop offset="0.55" stop-color="#f1e6e4"/>
          <stop offset="1" stop-color="#ead6d1"/>
        </linearGradient>
        <radialGradient id="heroWarm" cx="0.45" cy="0.55" r="0.5">
          <stop offset="0" stop-color="#efc4bd"/>
          <stop offset="1" stop-color="#efc4bd" stop-opacity="0"/>
        </radialGradient>
        <radialGradient id="heroHands" cx="0.75" cy="0.8" r="0.45">
          <stop offset="0" stop-color="#f0cdbd"/>
          <stop offset="1" stop-color="#f0cdbd" stop-opacity="0"/>
        </radialGradient>
        <clipPath id="heroCurve"><path d="M0 0 H370 V200 Q185 272 0 200 Z"/></clipPath>
      </defs>
      <g clip-path="url(#heroCurve)">
        <rect width="370" height="236" fill="url(#heroBase)"/>
        <rect width="370" height="236" fill="url(#heroWarm)"/>
        <rect width="370" height="236" fill="url(#heroHands)"/>
      </g>
    </svg>

    <div class="status-bar">
      <div class="signal"><i style="height:3px"></i><i style="height:5px"></i><i style="height:7px"></i><i style="height:9px"></i></div>
      <div class="clock">9:41 AM</div>
      <div class="battery">100% <div class="battery-cell"><span></span></div></div>
    </div>

    <svg class="back-arrow" width="16" height="24" viewBox="0 0 16 24" aria-label="Back">
      <polyline points="12,3 3,12 12,21" fill="none" stroke="#2f2a3d" stroke-width="2.4" stroke-linecap="round" stroke-linejoin="round"/>
    </svg>

    <svg class="play-button" width="50" height="50" viewBox="0 0 50 50" aria-label="Play video">
      <circle cx="25" cy="25" r="25" fill="#6e4aa3"/>
      <polygon points="20,15 35,25 20,35" fill="#ffffff"/>
    </svg>

    <h1 class="article-title">Growing Pains</h1>
    <div class="category-badge" role="img" aria-label="Baby category badge"></div>

    <p class="article-text intro">This is some text about the specific imbalance. What could be the reasons for it, is it normal/abnormal, symptoms etc.</p>

    <div class="inline-photo" role="img" aria-label="Photo of a parent massaging a baby's feet"></div>

    <p class="article-text tips">There are multiple ways to trigger some positive effects and you can try out multiple spots/treatments...</p>
  </main>

  <aside class="app-identity">
    <div class="app-tile" role="img" aria-label="App icon"></div>
    <div class="app-name">Rør og ro</div>
  </aside>

</body>
</html>
```